Wix Website design for my therapy business - Willowmere Group

I have started designing a Wix site and have a good idea of what I want.
I have set up the pages, created some design ideas, and inputted the copy. I need someone fabulous to finish off the design aspects. I like working closely with the designers, I was an interior designer in an old career.
I would like the site to be funky but professional. My Wix skills are limited, and I just can't achieve the look I am wanting without having to spend a lot of time learning. If it's easier to start over, that's ok providing you use the same colours, font, images etc. I have included a screenshot of the home page below. I have another site I need to start as soon as we have finished this one.
I am looking for someone who is a good listener and is has design flare. I am easy to get along with and will respond quickly.
I would like to set up SEO and have help in the future.
Let me know if you are the right person for the job.
Target Market(s)
Please needing help with their mental health and for therapy.
Industry/Entity Type
Mental health
Font styles to use
Other font styles liked:
- Futura light
Requirements
Must have
- be easy to navigate and be simple yet stylish
Nice to have
- I have set up the basics of the site - nice to haves are already on the site
Should not have
- old fashioned large chunks of text.

```html
<!DOCTYPE html>
<html lang="en">
<head>
<meta charset="utf-8">
<title>Willowmere Group – Therapy &amp; Counselling</title>
<link href="https://fonts.googleapis.com/css2?family=Jost:wght@300;400;500;700;800&family=Noto+Serif:wght@400&display=swap" rel="stylesheet">
<style>
:root{
  --brown:#9c8567;
  --brown-dark:#7d6950;
  --ink:#111111;
  --black:#000000;
  --white:#ffffff;
  --muted:#6b6b6b;
  --line:#cfcfcf;
  --star:#f5b400;
  --quote:#2f3a1c;
}
*{margin:0;padding:0;box-sizing:border-box}
html,body{width:1200px;height:3453px;overflow:hidden}
body{position:relative;font-family:"Jost",sans-serif;color:var(--ink);background:var(--white)}
.abs{position:absolute}
a{color:inherit;text-decoration:none}

/* top bar & nav */
.topline{left:0;top:0;width:1200px;height:3px;background:var(--brown)}
.nav a{position:absolute;top:34px;transform:translateX(-50%);font-size:15px;font-weight:400;white-space:nowrap;letter-spacing:.3px}
.brand-nav{position:absolute;left:600px;top:22px;transform:translateX(-50%);width:130px;text-align:center;font-size:18px;line-height:19px;font-weight:500;color:var(--brown)}

/* hero */
.hero-art{left:0;top:91px}
.hero-title{left:100px;top:160px;font-size:52px;font-weight:300;line-height:1}
.hero-name{left:100px;top:238px;font-size:56px;font-weight:800;line-height:1;letter-spacing:.5px}
.hero-sub{left:100px;top:310px;width:400px;font-size:17px;font-weight:300;line-height:30px;color:#333}

/* buttons */
.btn{position:absolute;z-index:1;display:flex;align-items:center;justify-content:center;gap:10px;font-size:22px;font-weight:400;color:var(--ink)}
.btn::before,.btn::after{content:"";position:absolute;inset:0;transform:skewX(-18deg)}
.btn::before{background:var(--brown);z-index:-1}
.btn::after{border:2px dashed var(--ink);border-top:none;border-left:none;left:6px;top:6px;right:-6px;bottom:-6px;z-index:-2}
.btn svg{width:19px;height:19px}
.btn-hero{left:110px;top:386px;width:210px;height:56px}
.btn-about{left:622px;top:1160px;width:214px;height:56px}
.btn-reviews{left:458px;top:2725px;width:286px;height:58px}

/* about */
.about-frame{left:87px;top:767px;width:443px;height:453px;border:2px dashed var(--brown);border-radius:80px 0 120px 0}
.about-photo{left:98px;top:775px;width:441px;height:452px;border-radius:80px 0 120px 0;background:linear-gradient(120deg,#d9d3cb 0%,#8a5f55 38%,#4b2f32 52%,#c9b6a9 70%,#a86a48 100%)}
.section-title{font-size:46px;font-weight:400;line-height:1;letter-spacing:.5px}
.about-title{left:617px;top:785px}
.rule{height:3px;background:var(--brown)}
.about-rule{left:617px;top:856px;width:131px}
.about-text{left:617px;top:889px;width:472px;font-size:19px;line-height:34.4px;font-weight:400}

/* services */
.services-art{left:0;top:1342px}
.services-title{left:0;top:1412px;width:1200px;text-align:center;color:var(--white)}
.service{position:absolute;top:1546px;width:316px}
.service-photo{width:316px;height:231px;border-radius:4px}
.service-name{margin-top:20px;text-align:center;font-size:27px;color:var(--white);font-weight:400}
.arrow{position:absolute;top:1647px;width:29px;height:29px}

/* reviews */
.reviews-title{left:0;top:2227px;width:1200px;text-align:center}
.reviews-rule{left:528px;top:2289px;width:144px}
.review{position:absolute;top:2349px;width:313px;height:286px;border:2px solid var(--line);border-radius:22px;background:var(--white)}
.review .q{position:absolute;left:20px;top:30px}
.review p{position:absolute;left:20px;top:74px;width:276px;font-family:"Noto Serif",serif;font-size:15px;line-height:22.4px;color:var(--muted)}
.review .stars{position:absolute;left:20px;top:207px;display:flex;gap:3px}
.review .name{position:absolute;left:20px;top:230px;font-size:23px;letter-spacing:4px;font-weight:400}
.review .avatar{position:absolute;left:196px;top:236px;width:76px;height:76px;border-radius:50%;background:radial-gradient(circle at 50% 45%,#b58e78,#6b5a4f 70%,#dcdcdc 72%)}

/* footer */
.footer-art{left:0;top:2836px}
.foot{color:var(--white)}
.foot-brand{left:94px;top:3072px;font-size:44px;font-weight:500;line-height:1;color:var(--brown);width:300px}
.foot-h{font-size:27px;font-weight:300;letter-spacing:.3px}
.foot-news{left:97px;top:3200px}
.foot-input{left:97px;top:3263px;width:291px;height:46px;border:1px solid var(--white);display:flex;align-items:center;justify-content:space-between;padding:0 12px;font-size:12px}
.foot-links-h{left:483px;top:3062px}
.foot-links{font-size:17px;font-weight:300;line-height:32px;list-style:none}
.foot-col1{left:488px;top:3110px}
.foot-col2{left:665px;top:3110px}
.foot-loc-h{left:884px;top:3058px}
.loc{position:absolute;left:880px;display:flex;align-items:center;gap:13px;font-size:15px;font-weight:300;line-height:22px;color:var(--white)}
.loc svg{flex:none}
.foot-rule{left:111px;top:3342px;width:978px;height:1px;background:#7a7a7a}
.copy{left:0;top:3374px;width:1200px;text-align:center;font-size:17px;font-weight:400;color:var(--white)}
</style>
</head>
<body>
<div class="abs topline"></div>

<nav class="nav">
  <a href="#" style="left:118px">Home</a>
  <a href="#" style="left:200px">About Us</a>
  <a href="#" style="left:321px">EMDR Addictions</a>
  <a href="#" style="left:463px">BetrayalTrauma</a>
  <span class="brand-nav">Willowmere Group</span>
  <a href="#" style="left:708px">Ptsd</a>
  <a href="#" style="left:794px">Program List</a>
  <a href="#" style="left:900px">Resources</a>
  <a href="#" style="left:979px">Blog</a>
  <a href="#" style="left:1062px">Contact Us</a>
</nav>

<!-- hero -->
<svg class="abs hero-art" width="1200" height="630" viewBox="0 0 1200 630" role="img" aria-label="Photo of two women talking in a bright therapy room">
  <defs>
    <linearGradient id="heroFill" x1="0" y1="0" x2="1" y2="0">
      <stop offset="0" stop-color="#f3f5f7"/>
      <stop offset="0.45" stop-color="#dde4ea"/>
      <stop offset="0.68" stop-color="#9aa5a8"/>
      <stop offset="0.82" stop-color="#6b5f52"/>
      <stop offset="1" stop-color="#d99583"/>
    </linearGradient>
  </defs>
  <rect width="1200" height="630" fill="url(#heroFill)"/>
  <polygon points="0,452 939,519 1200,419 1200,630 0,630" fill="var(--brown)"/>
  <polygon points="0,452 986,620 1200,425 1200,630 0,630" fill="var(--white)"/>
</svg>
<h2 class="abs hero-title">Welcome to</h2>
<h1 class="abs hero-name">WILLOWMERE GROUP</h1>
<p class="abs hero-sub">Sed ut perspiciatis unde omnis iste natus error sit voluptatem accusantium</p>
<a href="#" class="btn btn-hero">Get Started
  <svg viewBox="0 0 20 20"><circle cx="10" cy="10" r="10" fill="var(--ink)"/><path d="M8 5.5l4.5 4.5L8 14.5" stroke="var(--brown)" stroke-width="2.4" fill="none"/></svg></a>

<!-- about -->
<div class="abs about-frame"></div>
<div class="abs about-photo" role="img" aria-label="Photo of a smiling therapist taking notes during a session"></div>
<h2 class="abs section-title about-title">ABOUT US</h2>
<div class="abs rule about-rule"></div>
<p class="abs about-text">Nemo enim ipsam voluptatem quia voluptas sit aspernatur aut odit aut fugit, sed quia consequuntur magni dolores eos qui ratione voluptatem sequi nesciunt. Neque porro quisquam est, qui dolorem ipsum quia dolor sit amet, consectetur, adipisci velit, sed quia non numquam eius modi tempora incidunt ut labore et dolore magnam aliquam quaerat voluptatem.</p>
<a href="#" class="btn btn-about">Read More
  <svg viewBox="0 0 20 20"><circle cx="10" cy="10" r="10" fill="var(--ink)"/><path d="M8 5.5l4.5 4.5L8 14.5" stroke="var(--brown)" stroke-width="2.4" fill="none"/></svg></a>

<!-- services -->
<svg class="abs services-art" width="1200" height="800" viewBox="0 0 1200 800" role="img" aria-label="Soft background photo of a counselling session tinted brown">
  <defs>
    <linearGradient id="svcFill" x1="0" y1="0" x2="1" y2="1">
      <stop offset="0" stop-color="#a08a6d"/>
      <stop offset="0.5" stop-color="#96805f"/>
      <stop offset="1" stop-color="#a59073"/>
    </linearGradient>
  </defs>
  <polygon points="0,0 1200,0 1200,482 221,786 0,602" fill="var(--ink)"/>
  <polygon points="0,0 1200,0 1200,482 235,716 0,602" fill="url(#svcFill)"/>
</svg>
<h2 class="abs section-title services-title">OUR SERVICES</h2>
<div class="service" style="left:98px"><div class="service-photo" role="img" aria-label="Photo of a therapist guiding an EMDR session" style="background:linear-gradient(100deg,#1d1f26 0%,#2d3243 40%,#7d8fae 65%,#a9825c 100%)"></div><div class="service-name">EMDR</div></div>
<div class="service" style="left:441px"><div class="service-photo" role="img" aria-label="Photo of a man resting his head beside glasses of beer" style="background:linear-gradient(180deg,#3d4450 0%,#5a5e68 45%,#b58a52 75%,#6a4a30 100%)"></div><div class="service-name">Addictions</div></div>
<div class="service" style="left:782px"><div class="service-photo" role="img" aria-label="Photo of a distressed woman sitting on a grey sofa" style="background:linear-gradient(120deg,#e8e3dc 0%,#c9c5bf 45%,#a9a39b 70%,#dcd7d0 100%)"></div><div class="service-name">Betrayal Trauma</div></div>
<svg class="arrow" style="left:40px" viewBox="0 0 29 29"><circle cx="14.5" cy="14.5" r="14.5" fill="var(--white)"/><path d="M17 8.5l-6 6 6 6" stroke="#5a4a38" stroke-width="3" fill="none"/></svg>
<svg class="arrow" style="left:1125px" viewBox="0 0 29 29"><circle cx="14.5" cy="14.5" r="14.5" fill="var(--white)"/><path d="M12 8.5l6 6-6 6" stroke="#5a4a38" stroke-width="3" fill="none"/></svg>

<!-- reviews -->
<h2 class="abs section-title reviews-title">REAL REVIEWS FROM CLIENTS</h2>
<div class="abs rule reviews-rule"></div>

<div class="review" style="left:99px">
  <svg class="q" width="28" height="24" viewBox="0 0 28 24"><path d="M0 24V13C0 5 4 1 11 0v5c-3 1-5 3-5 7h5v12zM16 24V13c0-8 4-12 11-13v5c-3 1-5 3-5 7h5v12z" fill="var(--quote)"/></svg>
  <p>Lorem ipsum dolor sit amet, consectetur adipiscing elit, sed do eiusmod tempor incididunt ut labore et dolore magna aliqua. Ut enim ad minim veniam, quis nostrud</p>
  <div class="stars"><svg width="94" height="16" viewBox="0 0 94 16"><g fill="var(--star)"><path id="st" d="M8 0l2.4 5 5.6.6-4.2 3.8 1.2 5.6L8 12.2 3 15l1.2-5.6L0 5.6 5.6 5z"/><use href="#st" x="19.5"/><use href="#st" x="39"/><use href="#st" x="58.5"/><use href="#st" x="78"/></g></svg></div>
  <div class="name">Jhone Deo</div>
  <div class="avatar" role="img" aria-label="Portrait photo of the reviewer"></div>
</div>
<div class="review" style="left:443px">
  <svg class="q" width="28" height="24" viewBox="0 0 28 24"><path d="M0 24V13C0 5 4 1 11 0v5c-3 1-5 3-5 7h5v12zM16 24V13c0-8 4-12 11-13v5c-3 1-5 3-5 7h5v12z" fill="var(--quote)"/></svg>
  <p>Lorem ipsum dolor sit amet, consectetur adipiscing elit, sed do eiusmod tempor incididunt ut labore et dolore magna aliqua. Ut enim ad minim veniam, quis nostrud</p>
  <div class="stars"><svg width="94" height="16" viewBox="0 0 94 16"><g fill="var(--star)"><use href="#st"/><use href="#st" x="19.5"/><use href="#st" x="39"/><use href="#st" x="58.5"/><use href="#st" x="78"/></g></svg></div>
  <div class="name">Olive Yew</div>
  <div class="avatar" role="img" aria-label="Portrait photo of the reviewer"></div>
</div>
<div class="review" style="left:786px">
  <svg class="q" width="28" height="24" viewBox="0 0 28 24"><path d="M0 24V13C0 5 4 1 11 0v5c-3 1-5 3-5 7h5v12zM16 24V13c0-8 4-12 11-13v5c-3 1-5 3-5 7h5v12z" fill="var(--quote)"/></svg>
  <p>Lorem ipsum dolor sit amet, consectetur adipiscing elit, sed do eiusmod tempor incididunt ut labore et dolore magna aliqua. Ut enim ad minim veniam, quis nostrud</p>
  <div class="stars"><svg width="94" height="16" viewBox="0 0 94 16"><g fill="var(--star)"><use href="#st"/><use href="#st" x="19.5"/><use href="#st" x="39"/><use href="#st" x="58.5"/><use href="#st" x="78"/></g></svg></div>
  <div class="name">Teri Dactyl</div>
  <div class="avatar" role="img" aria-label="Portrait photo of the reviewer"></div>
</div>

<a href="#" class="btn btn-reviews">View All Reviews&nbsp;&nbsp;
  <svg viewBox="0 0 20 20"><circle cx="10" cy="10" r="10" fill="var(--ink)"/><path d="M8 5.5l4.5 4.5L8 14.5" stroke="var(--brown)" stroke-width="2.4" fill="none"/></svg></a>

<!-- footer -->
<svg class="abs footer-art" width="1200" height="617" viewBox="0 0 1200 617" aria-hidden="true">
  <polygon points="0,201 215,0 1200,168 1200,617 0,617" fill="var(--brown)"/>
  <polygon points="0,201 235,67 1200,168 1200,617 0,617" fill="var(--black)"/>
</svg>
<div class="abs foot-brand">Willowmere<br>Group</div>
<h3 class="abs foot foot-h foot-news">SUBSCRIBE NEWSLETTER</h3>
<div class="abs foot foot-input"><span>Email Address</span>
  <svg width="18" height="16" viewBox="0 0 18 16"><path d="M0 7L18 0 14 16 9 11 7 16 7 10 15 2 5 9z" fill="var(--white)"/></svg></div>

<h3 class="abs foot foot-h foot-links-h">QUICK LINK</h3>
<ul class="abs foot foot-links foot-col1"><li>Home</li><li>About Us</li><li>EMDR</li><li>Addictions</li><li>Betrayal Trauma</li><li>Ptsd</li></ul>
<ul class="abs foot foot-links foot-col2"><li>Program List</li><li>Resources</li><li>Blog</li><li>Contact Us</li></ul>

<h3 class="abs foot foot-h foot-loc-h">OUR LOCATION</h3>
<div class="loc" style="top:3118px"><svg width="32" height="32" viewBox="0 0 32 32"><circle cx="16" cy="16" r="15" fill="none" stroke="var(--white)" stroke-width="1.5"/><path d="M16 24s-5-5.5-5-9a5 5 0 0110 0c0 3.5-5 9-5 9z" fill="none" stroke="var(--white)" stroke-width="1.5"/><circle cx="16" cy="15" r="1.7" fill="var(--white)"/></svg><span style="font-size:14px">61 Lorem ipsum dolor sit amet,<br>consectetur</span></div>
<div class="loc" style="top:3192px"><svg width="32" height="32" viewBox="0 0 32 32"><circle cx="16" cy="16" r="15" fill="none" stroke="var(--white)" stroke-width="1.5"/><path d="M11 9l3 0 1.5 4-2 1.5a9 9 0 004 4l1.5-2 4 1.5v3c-7 1-13-5-12-12z" fill="none" stroke="var(--white)" stroke-width="1.5"/></svg><span>+1&nbsp;&nbsp; 888-888-8888</span></div>
<div class="loc" style="top:3251px"><svg width="32" height="32" viewBox="0 0 32 32"><circle cx="16" cy="16" r="15" fill="none" stroke="var(--white)" stroke-width="1.5"/><rect x="9" y="11" width="14" height="10" fill="none" stroke="var(--white)" stroke-width="1.5"/><path d="M9 11l7 6 7-6" fill="none" stroke="var(--white)" stroke-width="1.5"/></svg><span>info@willowmeregroup.com</span></div>

<div class="abs foot-rule"></div>
<p class="abs copy">© copyrights 2023 The Willowmere Group |&nbsp;&nbsp; All Rights Reserved</p>
</body>
</html>
```